Our companies name is The Gilded Ladle and we specialize in craft cupcakes, what I mean by that is that we bake our cupcakes with craft beer and other alcoholic drinks. We are trying to focus on being elegant but at the same time unpretentious. Since we are incorporating beer in our cupcakes we want the business card to have our logo in the front and our information in the back.

Once we select the best design we will provide the contact information to be added. Thank you.

Industry/Entity Type

Business

Font styles to use
Decorative
Script

Requirements
Must have
• Round corners
Should not have
• Square corners

```html
<!DOCTYPE html>
<html lang="en">
<head>
<meta charset="utf-8">
<title>The Gilded Ladle – Business Card</title>
<link rel="stylesheet" href="https://fonts.googleapis.com/css2?family=Exo+2:ital,wght@0,400;0,600;1,400&display=swap">
<style>
  :root {
    --backdrop-top: #a9afb9;
    --backdrop-bottom: #d3d7dd;
    --card-white: #f4f4f4;
    --card-shade: #e2e2e2;
    --ink-black: #0d0d0d;
    --ink-dark: #1c1c1c;
    --ink-grey: #555555;
    --accent-orange: #f0592a;
    --accent-red: #d92b2b;
    --text-light: #f2f2f2;
  }
  * { box-sizing: border-box; margin: 0; padding: 0; }
  html, body { width: 1200px; height: 866px; overflow: hidden; }
  body {
    background: linear-gradient(160deg, var(--backdrop-top), var(--backdrop-bottom));
    font-family: "Exo 2", sans-serif;
    position: relative;
  }
  .card {
    position: absolute;
    width: 540px;
    height: 309px;
    border-radius: 18px;
    overflow: hidden;
    background: radial-gradient(circle at 50% 45%, #ffffff, var(--card-white) 55%, var(--card-shade));
    box-shadow: 0 14px 30px rgba(0,0,0,0.22);
  }
  .card-front { left: 40px; top: 200px; }
  .card-back { left: 620px; top: 357px; }

  .brand-mark {
    display: flex;
    align-items: center;
    gap: 10px;
    font-weight: 600;
    color: var(--ink-dark);
    white-space: nowrap;
  }
  .brand-dot {
    width: 16px; height: 16px;
    border-radius: 50%;
    background: var(--accent-red);
    flex: none;
  }
  .card-front .brand-mark {
    position: absolute;
    left: 50%; top: 50%;
    transform: translate(-50%, -50%);
    font-size: 30px;
  }

  .back-shape { position: absolute; inset: 0; width: 100%; height: 100%; }
  .card-back .brand-mark {
    position: absolute;
    left: 28px; top: 118px;
    font-size: 19px;
  }
  .card-back .brand-dot { width: 12px; height: 12px; }

  .holder {
    position: absolute;
    right: 28px; top: 50px;
    text-align: right;
  }
  .holder-name {
    font-size: 20px;
    letter-spacing: 1px;
    color: var(--ink-black);
    text-transform: uppercase;
  }
  .holder-role {
    font-size: 13px;
    font-style: italic;
    color: var(--ink-grey);
  }

  .address, .website {
    position: absolute;
    right: 28px;
    text-align: right;
    color: var(--text-light);
    font-size: 12px;
    line-height: 1.45;
  }
  .address { top: 162px; }
  .website { top: 220px; letter-spacing: 0.5px; }

  .contact-list {
    position: absolute;
    left: 26px; bottom: 14px;
    list-style: none;
    color: var(--text-light);
    font-size: 11px;
    line-height: 1.5;
  }
  .contact-list li { display: flex; align-items: center; gap: 8px; }
  .contact-list svg { width: 11px; height: 11px; fill: var(--text-light); flex: none; }
</style>
</head>
<body>

<section class="card card-front" aria-label="Business card front">
  <div class="brand-mark"><span class="brand-dot"></span>The Gilded Ladle</div>
</section>

<section class="card card-back" aria-label="Business card back">
  <svg class="back-shape" viewBox="0 0 540 309" preserveAspectRatio="none" aria-hidden="true">
    <path d="M0,220 C180,195 380,155 540,118 L540,309 L0,309 Z" fill="var(--ink-black)"/>
    <path d="M0,208 C180,180 370,135 468,86 C392,140 232,192 0,216 Z" fill="var(--accent-orange)"/>
  </svg>

  <div class="brand-mark"><span class="brand-dot"></span>The Gilded Ladle</div>

  <div class="holder">
    <p class="holder-name">Mara Whitfield</p>
    <p class="holder-role">Managing Director</p>
  </div>

  <p class="address">27 Cellar Lane, Maple Court<br>Hollis</p>
  <p class="website">www.gildedladle.com</p>

  <ul class="contact-list">
    <li><svg viewBox="0 0 12 12"><path d="M2,1 L4,1 L5,4 L3.5,5 C4.3,6.7 5.3,7.7 7,8.5 L8,7 L11,8 L11,10 C11,10.6 10.6,11 10,11 C5,11 1,7 1,2 C1,1.4 1.4,1 2,1 Z"/></svg>014 258 3690</li>
    <li><svg viewBox="0 0 12 12"><path d="M3,0 H9 V12 H3 Z M4,1.5 V9 H8 V1.5 Z"/></svg>014 258 3691</li>
    <li><svg viewBox="0 0 12 12"><path d="M1,4 H11 V11 H1 Z M3,0 H9 V3 H3 Z"/></svg>014 258 3692</li>
    <li><svg viewBox="0 0 12 12"><path d="M0,2 H12 V10 H0 Z M1,3 L6,6.5 L11,3 Z" fill-rule="evenodd"/></svg>hello@gildedladle.com</li>
  </ul>
</section>

</body>
</html>
```